Beautify our counselling web application

I have a web application in development and at the moment it is very plain.
It has being developed with laravel and vue. I need a simple design for the user interface to make it look more sleek and professional. I will need someone who is able to code the design as part of the service. The app is very low-cost for voluntary and social enterprise services and we don't have a lot of money so I need someone who is just starting out or someone with a big heart.
I have uploaded current pages to show the contents.
I will tip for good work.

Target Market(s)

Counsellors and psychotherapists

Industry/Entity Type

SaaS

Font styles to use
Serif
Sans Serif

Colors
0054AA
0677BA
7BADD7
CADEEF
E8F1F8

Requirements
Must have
• Ability to code the design into the current site
Nice to have
• elegant, modern. cool, profession. nice examples include brintaloft.com quelvanote.com morvend.com
Should not have
• corny literal 90s icons, icons with more than one colour using primary colours

```html
<!DOCTYPE html>
<html lang="en">
<head>
<meta charset="utf-8">
<title>Counselling App – Screens</title>
<link rel="stylesheet" href="https://fonts.googleapis.com/css2?family=Poppins:wght@400;500;600;700&display=swap">
<style>
:root{
  --brand:#0054aa;
  --navy:#2f3b55;
  --ink:#1f2a3d;
  --text:#333a45;
  --muted:#6b7280;
  --link:#6a5cf0;
  --risk:#1fbf75;
  --line:#e3e6ea;
  --canvas:#ffffff;
  --panel-bg:#f2f2f4;
  --tab-light:#cadeef;
  --tab-light-ink:#3d5a80;
}
*{box-sizing:border-box;margin:0;padding:0}
html,body{width:1200px;height:2625px;overflow:hidden;background:var(--canvas);font-family:"Poppins",sans-serif;color:var(--text)}
.screen{position:absolute;left:108px;width:962px;height:715px;background:#fff;box-shadow:0 4px 14px rgba(0,0,0,.18);overflow:hidden}
.screen--caseload{top:113px}
.screen--dashboard{top:931px}
.screen--workspace{top:1748px}
.sidebar{position:absolute;left:0;top:0;width:149px;height:100%;border-right:1px solid var(--line);background:#fff}
.brand{position:absolute;left:3px;top:14px;font-weight:700;font-size:14.5px;letter-spacing:.3px;color:var(--ink);white-space:nowrap}
.nav{position:absolute;left:14px;top:72px;width:122px;list-style:none}
.nav li{height:45px;line-height:30px;font-size:11.5px;color:var(--ink);padding-left:8px;display:flex;align-items:flex-start}
.nav li span{display:block;height:31px;line-height:31px;white-space:nowrap}
.nav li.active span{background:var(--brand);color:#fff;border-radius:3px;width:122px;padding-left:27px;position:relative;margin-left:-8px;font-weight:500}
.nav li.active svg{position:absolute;left:9px;top:8px}
.topbar{position:absolute;left:149px;right:0;top:0;height:62px}
.topbar .rule{position:absolute;left:0;right:30px;bottom:0;height:1px;background:var(--line)}
.search{position:absolute;left:18px;top:7px;width:347px;height:34px;border-radius:17px;box-shadow:0 1px 4px rgba(0,0,0,.14);display:flex;align-items:center;font-size:10.5px}
.search .filter{margin-left:20px;color:var(--ink)}
.search .filter:after{content:"⌄";font-size:9px;margin-left:5px;position:relative;top:-2px}
.search .hint{margin-left:24px;color:#8b8f96}
.search .glass{position:absolute;right:11px;top:9px;width:16px;height:16px;border-radius:50%;background:#e4e6ea}
.tools{position:absolute;right:15px;top:13px;display:flex;align-items:center;gap:8px}
.tool{width:17px;height:17px;border-radius:50%;background:#eceef1;font-size:9px;display:flex;align-items:center;justify-content:center;color:var(--ink)}
.user{height:23px;width:92px;border-radius:12px;box-shadow:0 1px 3px rgba(0,0,0,.2);display:flex;align-items:center;font-size:6.5px;color:var(--ink);padding-left:3px;gap:4px;white-space:nowrap}
.avatar{width:17px;height:17px;border-radius:50%;background:radial-gradient(circle at 50% 40%,#d9b59a,#7a5a48)}
.content{position:absolute;left:168px;top:74px;right:0}
h1{font-size:19.5px;font-weight:700;color:var(--navy)}
.caseload{position:absolute;left:168px;top:118px;border-collapse:collapse;font-size:8.5px}
.caseload th{font-weight:500;color:var(--ink);text-align:left;height:12px;padding:0;white-space:nowrap}
.caseload td{height:45.6px;padding:0;color:var(--text);vertical-align:top;padding-top:21px;white-space:nowrap}
.caseload td.client{color:var(--link)}
.dot{display:inline-block;width:6px;height:6px;border-radius:50%;background:var(--risk);margin:5px 0 0 6px}
.contacts{display:inline-flex;align-items:center;gap:6px;width:70px;height:26px;margin-top:-8px;border-radius:3px;box-shadow:0 1px 3px rgba(0,0,0,.18);padding-left:12px;font-size:8px}
.contacts:before{content:"";border-left:6px solid var(--ink);border-top:4px solid transparent;border-bottom:4px solid transparent}
.welcome{position:absolute;left:168px;top:125px;width:334px;height:47px;border-radius:4px;background:var(--navy);color:#fff;font-size:12px;font-weight:500;display:flex;align-items:center;justify-content:center}
.block{position:absolute;left:150px;width:237px;border-top:1px solid var(--line);padding-left:18px}
.block h2{font-size:15.5px;font-weight:600;color:var(--navy)}
.block p{font-size:11px;color:var(--ink)}
.btn{display:inline-flex;align-items:center;justify-content:center;border-radius:3px;font-size:11.5px;color:#fff;background:var(--brand);font-weight:500;white-space:nowrap}
.stage{position:absolute;left:149px;top:62px;right:0;bottom:0;background:var(--panel-bg)}
.crumb{position:absolute;left:20px;top:16px;font-size:19px;font-weight:700;color:var(--navy);white-space:nowrap;letter-spacing:-.3px}
.tab{position:absolute;top:12px;height:32px;border-radius:3px;font-size:10px;display:flex;align-items:center;justify-content:center;white-space:nowrap}
.tab--solid{background:var(--brand);color:#fff}
.tab--soft{background:var(--tab-light);color:var(--tab-light-ink)}
.tab--ghost{border:1px solid #cfd3d8;color:#c2c6cc;background:#fff}
.episode{position:absolute;left:7px;top:97px;width:797px;height:169px;background:#fff;border-radius:2px}
.episode .name{position:absolute;left:13px;top:12px;font-size:12.5px;color:var(--ink)}
.episode .started{position:absolute;left:508px;top:14px;font-size:10.5px;color:var(--ink);white-space:nowrap}
.episode .started b{font-weight:600}
.tag{position:absolute;width:111px;height:31px;border-radius:3px;color:#fff;font-size:10px;display:flex;align-items:center;justify-content:center;white-space:nowrap}
</style>
</head>
<body>

<section class="screen screen--caseload">
  <aside class="sidebar">
    <div class="brand">COUNSELLING APP</div>
    <ul class="nav">
      <li><span>Dashboard</span></li>
      <li class="active"><span><svg width="14" height="14" viewBox="0 0 14 14" fill="none" stroke="#fff" stroke-width="1.2"><path d="M2 1h7l3 3v9H2z"/><path d="M4 6h6M4 8.5h6M4 11h3"/></svg>Caseload</span></li>
      <li><span>Calendar</span></li><li><span>Address Book</span></li><li><span>Users</span></li><li><span>Services</span></li><li><span>Clients</span></li><li><span>Audit</span></li><li><span>Monitoring</span></li><li><span>Templates</span></li>
    </ul>
  </aside>
  <header class="topbar">
    <div class="search"><span class="filter">Filter</span><span class="hint">Search Everything</span><span class="glass"></span></div>
    <div class="tools"><span class="tool">?</span><span class="tool">⇥</span><span class="user"><span class="avatar" role="img" aria-label="User profile photo"></span>Aldo R Venn ⌄</span></div>
    <div class="rule"></div>
  </header>
  <div class="content"><h1>Caseload</h1></div>
  <table class="caseload">
    <colgroup><col style="width:49px"><col style="width:57px"><col style="width:94px"><col style="width:42px"><col style="width:101px"><col style="width:75px"><col style="width:101px"><col style="width:91px"><col style="width:101px"><col style="width:90px"></colgroup>
    <thead><tr><th>Risk</th><th>Alerts</th><th>Client</th><th>ID</th><th>Service</th><th>Therapist</th><th>Date of referral</th><th>First Contact</th><th>Previous Episode</th><th style="padding-left:10px">Contacts</th></tr></thead>
    <tbody>
      <tr><td><span class="dot"></span></td><td></td><td class="client">Helen Marsh</td><td>002</td><td>Demo Service 1</td><td>Dena</td><td>05/07/2022</td><td>20/09/2022</td><td></td><td><span class="contacts">Total: 3</span></td></tr>
      <tr><td><span class="dot"></span></td><td></td><td class="client">Helen Marsh</td><td>002</td><td>Demo Service 1</td><td>Dena</td><td>05/07/2022</td><td>20/09/2022</td><td></td><td><span class="contacts">Total: 3</span></td></tr>
      <tr><td><span class="dot"></span></td><td></td><td class="client">Helen Marsh</td><td>002</td><td>Demo Service 1</td><td>Dena</td><td>05/07/2022</td><td>20/09/2022</td><td></td><td><span class="contacts">Total: 3</span></td></tr>
      <tr><td><span class="dot"></span></td><td></td><td class="client">Helen Marsh</td><td>002</td><td>Demo Service 1</td><td>Dena</td><td>05/07/2022</td><td>20/09/2022</td><td></td><td><span class="contacts">Total: 3</span></td></tr>
      <tr><td><span class="dot"></span></td><td></td><td class="client">Helen Marsh</td><td>002</td><td>Demo Service 1</td><td>Dena</td><td>05/07/2022</td><td>20/09/2022</td><td></td><td><span class="contacts">Total: 3</span></td></tr>
      <tr><td><span class="dot"></span></td><td></td><td class="client">Helen Marsh</td><td>002</td><td>Demo Service 1</td><td>Dena</td><td>05/07/2022</td><td>20/09/2022</td><td></td><td><span class="contacts">Total: 3</span></td></tr>
      <tr><td><span class="dot"></span></td><td></td><td class="client">Helen Marsh</td><td>002</td><td>Demo Service 1</td><td>Dena</td><td>05/07/2022</td><td>20/09/2022</td><td></td><td><span class="contacts">Total: 3</span></td></tr>
      <tr><td><span class="dot"></span></td><td></td><td class="client">Helen Marsh</td><td>002</td><td>Demo Service 1</td><td>Dena</td><td>05/07/2022</td><td>20/09/2022</td><td></td><td><span class="contacts">Total: 3</span></td></tr>
      <tr><td><span class="dot"></span></td><td></td><td class="client">Helen Marsh</td><td>002</td><td>Demo Service 1</td><td>Dena</td><td>05/07/2022</td><td>20/09/2022</td><td></td><td><span class="contacts">Total: 3</span></td></tr>
      <tr><td><span class="dot"></span></td><td></td><td class="client">Helen Marsh</td><td>002</td><td>Demo Service 1</td><td>Dena</td><td>05/07/2022</td><td>20/09/2022</td><td></td><td><span class="contacts">Total: 3</span></td></tr>
      <tr><td><span class="dot"></span></td><td></td><td class="client">Helen Marsh</td><td>002</td><td>Demo Service 1</td><td>Dena</td><td>05/07/2022</td><td>20/09/2022</td><td></td><td><span class="contacts">Total: 3</span></td></tr>
      <tr><td><span class="dot"></span></td><td></td><td class="client">Helen Marsh</td><td>002</td><td>Demo Service 1</td><td>Dena</td><td>05/07/2022</td><td>20/09/2022</td><td></td><td><span class="contacts">Total: 3</span></td></tr>
    </tbody>
  </table>
</section>

<section class="screen screen--dashboard">
  <aside class="sidebar">
    <div class="brand">COUNSELLING APP</div>
    <ul class="nav">
      <li class="active"><span><svg width="14" height="14" viewBox="0 0 14 14" fill="none" stroke="#fff" stroke-width="1.2"><rect x="1" y="1" width="5" height="5"/><rect x="8" y="1" width="5" height="5"/><rect x="1" y="8" width="5" height="5"/><rect x="8" y="8" width="5" height="5"/></svg>Dashboard</span></li>
      <li><span>Caseload</span></li><li><span>Calendar</span></li><li><span>Address Book</span></li><li><span>Users</span></li><li><span>Services</span></li><li><span>Clients</span></li><li><span>Audit</span></li><li><span>Monitoring</span></li><li><span>Templates</span></li>
    </ul>
  </aside>
  <header class="topbar">
    <div class="search"><span class="filter">Filter</span><span class="hint">Search Everything</span><span class="glass"></span></div>
    <div class="tools"><span class="tool">?</span><span class="tool">⇥</span><span class="user"><span class="avatar" role="img" aria-label="User profile photo"></span>Aldo R Venn ⌄</span></div>
    <div class="rule"></div>
  </header>
  <div class="content" style="top:75px"><h1>Dashboard</h1></div>
  <div class="welcome">Welcom to Demo</div>
  <div class="block" style="top:186px;height:90px;padding-top:10px">
    <h2>Notifications</h2>
    <span class="btn" style="width:151px;height:32px;margin-top:4px">Create Notification</span>
  </div>
  <div class="block" style="top:276px;height:51px;padding-top:12px"><h2>No Notifications</h2></div>
  <div class="block" style="top:327px;height:71px;padding-top:11px"><h2>Today</h2><p>No appointments!</p></div>
  <div class="block" style="top:398px;padding-top:22px"><h2>Reviews</h2><p>No reviews!</p></div>
</section>

<section class="screen screen--workspace">
  <aside class="sidebar">
    <div class="brand">COUNSELLING APP</div>
    <ul class="nav">
      <li><span>Dashboard</span></li>
      <li class="active"><span><svg width="14" height="14" viewBox="0 0 14 14" fill="none" stroke="#fff" stroke-width="1.2"><path d="M2 1h7l3 3v9H2z"/><path d="M4 6h6M4 8.5h6M4 11h3"/></svg>Caseload</span></li>
      <li><span>Calendar</span></li><li><span>Address Book</span></li><li><span>Users</span></li><li><span>Services</span></li><li><span>Clients</span></li><li><span>Audit</span></li><li><span>Monitoring</span></li><li><span>Templates</span></li>
    </ul>
  </aside>
  <header class="topbar">
    <div class="search"><span class="filter">Filter</span><span class="hint">Search Everything</span><span class="glass"></span></div>
    <div class="tools"><span class="tool">?</span><span class="tool">⇥</span><span class="user"><span class="avatar" role="img" aria-label="User profile photo"></span>Aldo R Venn ⌄</span></div>
    <div class="rule"></div>
  </header>
  <div class="stage">
    <div class="crumb">Caseload / Helen Marsh</div>
    <div class="tab tab--solid" style="left:272px;width:99px">Workspace&nbsp;&nbsp;&nbsp;&nbsp;⌃</div>
    <div class="tab tab--solid" style="left:380px;width:112px">Client Information</div>
    <div class="tab tab--soft" style="left:502px;width:98px">Client Record</div>
    <div class="tab tab--soft" style="left:609px;width:99px">Client Progress</div>
    <div class="tab tab--ghost" style="left:716px;width:73px">Payments</div>
    <div class="episode">
      <div class="name">Episode 1</div>
      <div class="started"><b>Started:</b> Wed Sep 14 2022</div>
      <span class="btn" style="position:absolute;left:671px;top:6px;width:112px;height:32px;font-size:10px">End Episode</span>
      <span class="tag" style="left:8px;top:71px;background:#cf5d6e">Session Record</span>
      <span class="tag" style="left:141px;top:71px;background:#b8733e">Assessment</span>
      <span class="tag" style="left:273px;top:71px;background:#b5a92c">Risk Management</span>
      <span class="tag" style="left:406px;top:71px;background:#4e9a35">Treatment Plan</span>
      <span class="tag" style="left:539px;top:71px;background:#2f6e4d">Safeguarding</span>
      <span class="tag" style="left:671px;top:71px;background:#4c9ea0">Consent</span>
      <span class="tag" style="left:8px;top:112px;background:#4f6db8">Questionnaire</span>
      <span class="tag" style="left:141px;top:112px;background:#5a3bc9">Document</span>
      <span class="tag" style="left:273px;top:112px;background:#5e3461">Non-clinical note</span>
      <span class="tag" style="left:406px;top:112px;background:#a883a9">Summary</span>
      <span class="tag" style="left:539px;top:112px;background:#913796">Timeline</span>
    </div>
  </div>
</section>

</body>
</html>
```